Willowmere Spa and Beauty Ltd. (Name of business)

I need a business card designed for this new company based out of Toronto Ontario. We specialize in Eyelash Extensions, Manicures and Pedicures, body waxing, massages, laser hair removal and botox treatments. Also offer a variety of products for sale, such as skin cream serums, collagen gel, eye cream, etc. It is a safe relaxing and non-judgemental environnment. Clients are welcome to come be pampered for the half or full day. Many service packages to choose from.

Open 7days per week from 8am to 8pm.

Priscilla Dunmore
Spa Facilitator
Willowmere Spa and Beauty Ltd.
7200 Harcourt St; Suite 1400
Toronto ON K2P 9W4

OFFICE: 416.790.4100
FAX: 416.790.4101
CELL: 416.632.1987
EMAIL: priscilla.dunmore@willowmerespa.com

Target Market(s)

Target market is primarily female ranging from 16 years old to 50 years old.

Industry/Entity Type

Business

Contact Information for Business Card

Priscilla Dunmore
Spa Facilitator
7200 Harcourt St; Suite 1400
Toronto ON K2P 9W4

OFFICE: 416.790.4100
FAX: 416.790.4101
CELL: 416.632.1987

Logo Text

I dont have a logo yet. I would like it simple but sophisticated and modern.

Font styles to use
Serif

Requirements
Must have
• all pertinent details such as company name, logo, name and contact information, services that are offered, including package rates
Nice to have
• Company name and logo prominent. A card that is neat and the information such as address, phone number, fax, email, etc is not too crowded but laid out in an easy to read format.
• Possibly on the back of card - some of the services offered could be listed, as well as professional cream lotions and serums. Hours of operation etc.

```html
<!DOCTYPE html>
<html lang="en">
<head>
<meta charset="utf-8">
<title>Willowmere Spa and Beauty – Business Card</title>
<link href="https://fonts.googleapis.com/css2?family=Barlow:ital,wght@0,400;0,500;0,600;1,500&display=swap" rel="stylesheet">
<style>
  :root {
    --page-bg: #efe9e2;
    --card-white: #ffffff;
    --teal: #4fc4bd;
    --teal-dark: #3bb3ac;
    --pink-text: #ea5f7c;
    --crimson: #c93a5c;
    --petal-light: #f6b6c2;
    --petal-mid: #f08a9e;
    --petal-warm: #f7a07e;
    --shadow: rgba(0,0,0,0.28);
  }
  * { margin: 0; padding: 0; box-sizing: border-box; }
  html, body {
    width: 980px; height: 1200px; overflow: hidden;
    background: var(--page-bg);
    font-family: "Barlow", "Helvetica Neue", Arial, sans-serif;
  }
  .canvas { position: relative; width: 980px; height: 1200px; }

  .card {
    position: absolute;
    background: var(--card-white);
    box-shadow: 0 3px 10px var(--shadow);
    overflow: hidden;
  }
  .card svg.card-art { position: absolute; inset: 0; }

  /* Front card */
  .card-front { left: 138px; top: 190px; width: 704px; height: 400px; }
  .front-brand {
    position: absolute; left: 0; right: 0; top: 128px;
    display: flex; justify-content: center; align-items: center; gap: 12px;
    color: var(--teal-dark); font-size: 34px; font-weight: 600; letter-spacing: 1px;
  }
  .front-brand .brand-square {
    width: 22px; height: 22px; background: var(--pink-text);
  }
  .front-address {
    position: absolute; left: 0; right: 0; top: 218px;
    text-align: center; color: var(--pink-text);
    font-size: 20px; line-height: 26px; font-weight: 400;
  }
  .front-hours {
    position: absolute; left: 0; right: 0; top: 312px;
    text-align: center; color: var(--pink-text); font-size: 20px;
  }

  /* Back card */
  .card-back { left: 138px; top: 650px; width: 705px; height: 404px; }
  .person-name {
    position: absolute; left: 54px; top: 64px;
    color: var(--crimson); font-size: 37px; font-weight: 600; letter-spacing: 1px;
    text-transform: uppercase;
  }
  .person-title {
    position: absolute; left: 95px; top: 114px;
    color: var(--pink-text); font-size: 25px; font-style: italic; font-weight: 500;
    letter-spacing: 3px; text-transform: uppercase;
  }
  .contact-list {
    position: absolute; left: 58px; top: 180px;
    list-style: none; color: var(--pink-text); font-size: 19.5px; line-height: 26px;
  }
  .back-brand {
    position: absolute; left: 530px; width: 150px; top: 148px;
    text-align: center; color: var(--card-white); font-size: 24px; font-weight: 600;
  }
</style>
</head>
<body>
<main class="canvas">

  <section class="card card-front" aria-label="Business card front">
    <svg class="card-art" width="704" height="400" viewBox="0 0 704 400">
      <defs>
        <linearGradient id="floralFront" x1="0" y1="0" x2="1" y2="0">
          <stop offset="0" stop-color="var(--petal-light)"/>
          <stop offset="0.45" stop-color="var(--petal-mid)"/>
          <stop offset="1" stop-color="var(--petal-warm)"/>
        </linearGradient>
      </defs>
      <path role="img" aria-label="Soft pink and coral floral illustration"
            d="M0 0 H704 V165 Q352 30 0 165 Z" fill="url(#floralFront)"/>
      <path d="M0 165 Q352 42 704 165" fill="none" stroke="var(--teal)" stroke-width="6"/>
      <path d="M0 350 Q352 372 704 350 V400 H0 Z" fill="var(--teal)"/>
      <path d="M0 350 Q352 372 704 350" fill="none" stroke="rgba(0,0,0,0.15)" stroke-width="2"/>
    </svg>
    <div class="front-brand"><span class="brand-square"></span><span>Willowmere</span></div>
    <p class="front-address">Willowmere Spa and Beauty Ltd.<br>7200 Harcourt St; Suite 1400<br>Toronto ON K2P 9W4</p>
    <p class="front-hours">Open 7days per week from 8am to 8pm</p>
  </section>

  <section class="card card-back" aria-label="Business card back">
    <svg class="card-art" width="705" height="404" viewBox="0 0 705 404">
      <defs>
        <linearGradient id="floralBack" x1="0" y1="0" x2="0" y2="1">
          <stop offset="0" stop-color="var(--petal-light)"/>
          <stop offset="0.55" stop-color="var(--petal-mid)"/>
          <stop offset="1" stop-color="var(--petal-light)"/>
        </linearGradient>
      </defs>
      <path role="img" aria-label="Soft pink floral illustration"
            d="M438 0 H705 V404 H440 Q520 190 438 0 Z" fill="url(#floralBack)"/>
      <path d="M438 0 Q520 190 452 370" fill="none" stroke="var(--teal)" stroke-width="4"/>
      <path d="M0 340 Q352 380 705 340 V404 H0 Z" fill="var(--teal)"/>
      <path d="M0 340 Q352 380 705 340" fill="none" stroke="rgba(0,0,0,0.15)" stroke-width="2"/>
    </svg>
    <h1 class="person-name">Priscilla Dunmore</h1>
    <p class="person-title">Spa Facilitator</p>
    <ul class="contact-list">
      <li>OFFICE: 416.790.4100</li>
      <li>FAX: 416.790.4101</li>
      <li>CELL: 416.632.1987</li>
      <li>EMAIL: priscilla.dunmore@willowmerespa.com</li>
    </ul>
    <div class="back-brand">Willowmere</div>
  </section>

</main>
</body>
</html>
```